Hello Copper Lantern,

We would like a stationary design set that complements Brightpath Works' innovative and futuristic feel. Please refer to the website or the previous project for more information on Brightpath Works.

Please create a couple of concepts first so I know that you are on the right track.

```html
<!DOCTYPE html>
<html lang="en">
<head>
<meta charset="utf-8">
<title>Brightpath Works – Stationery Set</title>
<link href="https://fonts.googleapis.com/css2?family=Open+Sans:wght@300;400;600;700&family=Ubuntu:wght@500&display=swap" rel="stylesheet">
<style>
  :root {
    --blue: #1b7fdc;
    --blue-deep: #1a78d6;
    --sky: #8fd6f5;
    --grey: #9a9aa0;
    --grey-light: #d9d9dc;
    --ink: #2b2b2b;
    --ink-navy: #16324f;
    --paper: #ffffff;
    --label: #ffffff;
  }
  * { margin: 0; padding: 0; box-sizing: border-box; }
  html, body { width: 1067px; height: 1200px; overflow: hidden; }
  body {
    font-family: "Open Sans", sans-serif;
    background: linear-gradient(135deg, #2a2a2a 0%, #6e6e6e 40%, #b8b8b8 75%, #e6e6e6 100%);
    position: relative;
  }
  .view-label {
    position: absolute;
    color: var(--label);
    font-size: 22px;
    font-weight: 600;
    transform: translateX(-50%);
  }
  .sheet {
    position: absolute;
    background: var(--paper);
    overflow: hidden;
    box-shadow: 4px 6px 10px rgba(0,0,0,0.45);
  }
  .sheet > svg.backdrop { position: absolute; inset: 0; width: 100%; height: 100%; }
  .brand-name {
    position: absolute;
    font-family: "Open Sans", sans-serif;
    font-weight: 600;
    color: var(--blue);
    white-space: nowrap;
    letter-spacing: -0.3px;
  }

  .card-front { left: 29px; top: 146px; width: 493px; height: 294px; }
  .card-front .brand-name { left: 45px; top: 158px; font-size: 32px; }

  .card-back { left: 555px; top: 146px; width: 492px; height: 294px; }
  .card-back .brand-name { left: 48px; top: 116px; font-size: 22px; }
  .person-name {
    position: absolute; left: 274px; top: 136px;
    font-family: "Ubuntu", sans-serif; font-weight: 500; font-size: 20px;
    color: var(--paper); white-space: nowrap;
  }
  .person-title {
    position: absolute; left: 274px; top: 163px;
    font-size: 14px; font-weight: 300; color: #2a3a4a; white-space: nowrap;
  }
  .contact-list {
    position: absolute; left: 274px; top: 190px; list-style: none;
    color: var(--paper); font-size: 11.5px; line-height: 18.5px; white-space: nowrap;
  }
  .contact-list b { font-weight: 600; color: var(--ink-navy); }

  .letterhead { left: 340px; top: 569px; width: 409px; height: 573px; }
  .lh-contact {
    position: absolute; left: 44px; top: 49px; list-style: none;
    font-size: 5.8px; line-height: 9.3px; color: var(--ink); white-space: nowrap;
  }
  .lh-contact b { font-weight: 700; }
  .letterhead .brand-name { right: 20px; top: 74px; font-size: 14px; }
  .lh-heading { position: absolute; left: 44px; top: 139px; font-size: 12px; font-weight: 400; color: var(--ink); }
  .lh-body {
    position: absolute; left: 44px; top: 167px; width: 292px;
    font-size: 6.9px; line-height: 8.5px; color: var(--ink); text-align: justify;
  }
  .lh-body p + p { margin-top: 10.5px; }
  .lh-sign { position: absolute; left: 44px; top: 482px; }
  .lh-sign-name { font-size: 8.5px; font-weight: 600; color: var(--blue); }
  .lh-sign-title { font-size: 7px; color: var(--ink); margin-top: 2px; }
</style>
</head>
<body>
  <div class="view-label" style="left:262px; top:93px;">Front</div>
  <div class="view-label" style="left:800px; top:93px;">Back</div>
  <div class="view-label" style="left:545px; top:510px;">letterhead</div>

  <section class="sheet card-front">
    <svg class="backdrop" viewBox="0 0 554 331" preserveAspectRatio="none" aria-hidden="true">
      <defs>
        <linearGradient id="frontPanel" x1="0" y1="1" x2="1" y2="0">
          <stop offset="0.3" stop-color="#1b7fdc"/>
          <stop offset="1" stop-color="#94daf6"/>
        </linearGradient>
      </defs>
      <polygon points="510,0 370,331 554,331 554,0" fill="#a3a3a8"/>
      <polygon points="522,0 382,331 554,331 554,0" fill="url(#frontPanel)"/>
    </svg>
    <div class="brand-name">Brightpath Works</div>
  </section>

  <section class="sheet card-back">
    <svg class="backdrop" viewBox="0 0 554 331" preserveAspectRatio="none" aria-hidden="true">
      <defs>
        <linearGradient id="backPanel" x1="0" y1="1" x2="1" y2="0.4">
          <stop offset="0" stop-color="#8fd6f5"/>
          <stop offset="0.55" stop-color="#1e82de"/>
          <stop offset="1" stop-color="#1a78d6"/>
        </linearGradient>
      </defs>
      <polygon points="0,320 250,229 330,89 554,49 554,55 334,95 254,235 0,327" fill="#d6d6d9"/>
      <polygon points="0,327 254,235 334,95 554,55 554,331 0,331" fill="#9a9aa0"/>
      <polygon points="0,331 258,240 338,100 554,61 554,331" fill="url(#backPanel)"/>
    </svg>
    <div class="brand-name">Brightpath Works</div>
    <div class="person-name">Daniel Rourke</div>
    <div class="person-title">Chief Executive Officer</div>
    <ul class="contact-list">
      <li><b>Phone:</b> +1 (555) 318-2047</li>
      <li><b>Telephone:</b> +1 (555) 604-7712</li>
      <li><b>Website:</b> www.BrightpathWorks.com</li>
      <li><b>Email:</b> daniel@brightpathworks.com</li>
    </ul>
  </section>

  <section class="sheet letterhead">
    <svg class="backdrop" viewBox="0 0 460 645" preserveAspectRatio="none" aria-hidden="true">
      <polygon points="460,132 397,300 397,485 0,622 0,645 460,645" fill="#a0a0a6"/>
      <polygon points="460,142 405,300 405,490 0,632 0,645 460,645" fill="var(--blue-deep)"/>
    </svg>
    <ul class="lh-contact">
      <li><b>Phone:</b> +1 (555) 318-2047</li>
      <li><b>Telephone:</b> +1 (555) 604-7712</li>
      <li><b>Website:</b> www.BrightpathWorks.com</li>
      <li><b>Email:</b> daniel@brightpathworks.com</li>
    </ul>
    <div class="brand-name">Brightpath Works</div>
    <h1 class="lh-heading">LOREM IPSUM IS SIMPLY DUMMY TEXT</h1>
    <div class="lh-body">
      <p>Lorem ipsum dolor sit amet, consectetur adipiscing elit, sed do eiusmod tempor incididunt ut labore et dolore magna aliqua. Ut enim ad minim veniam, quis nostrud exercitation ullamco laboris nisi ut aliquip ex ea commodo consequat. Duis aute irure dolor in reprehenderit in voluptate velit esse cillum dolore eu fugiat nulla pariatur. Excepteur sint occaecat cupidatat non proident, sunt in culpa qui officia deserunt mollit anim id est laborum. Sed ut perspiciatis unde omnis iste natus error sit voluptatem accusantium doloremque laudantium, totam rem aperiam.</p>
      <p>Lorem ipsum dolor sit amet, consectetur adipiscing elit, sed do eiusmod tempor incididunt ut labore et dolore magna aliqua. Ut enim ad minim veniam, quis nostrud exercitation ullamco laboris nisi ut aliquip ex ea commodo consequat. Duis aute irure dolor in reprehenderit in voluptate velit esse cillum dolore eu fugiat nulla pariatur. Excepteur sint occaecat cupidatat non proident, sunt in culpa qui officia deserunt mollit anim id est laborum. Sed ut perspiciatis unde omnis iste natus error sit voluptatem accusantium doloremque laudantium, totam rem aperiam.</p>
      <p>Lorem ipsum dolor sit amet, consectetur adipiscing elit, sed do eiusmod tempor incididunt ut labore et dolore magna aliqua. Ut enim ad minim veniam, quis nostrud exercitation ullamco laboris nisi ut aliquip ex ea commodo consequat. Duis aute irure dolor in reprehenderit in voluptate velit esse cillum dolore eu fugiat nulla pariatur. Excepteur sint occaecat cupidatat non proident, sunt in culpa qui officia deserunt mollit anim id est laborum. Sed ut perspiciatis unde omnis iste natus error sit voluptatem accusantium doloremque laudantium, totam rem aperiam.</p>
    </div>
    <div class="lh-sign">
      <div class="lh-sign-name">Daniel Rourke</div>
      <div class="lh-sign-title">Chief Executive Officer</div>
    </div>
  </section>
</body>
</html>
```